Business Card for Trivelo, a french tech company

Tech company
New technologies
Serious design
Dark theme

User info :
Name: Florian GASTIER
Position: Co-Founder & CEO
Tel: (+33) 6 52 84 26 07
Email: florian@trivelo.example
Website: www.trivelo.example
Address: 17 rue des Tanneurs 69001 LYON

```html
<!DOCTYPE html>
<html lang="fr">
<head>
<meta charset="utf-8">
<title>Trivelo — Business Card</title>
<link href="https://fonts.googleapis.com/css2?family=Rubik:wght@500&family=Noto+Sans:wght@400;700&display=swap" rel="stylesheet">
<style>
  :root {
    --stage-dark: #121c2e;
    --stage-light: #ffffff;
    --card-top: #150a44;
    --card-mid: #110c48;
    --card-bottom: #15306b;
    --back-top: #1b5585;
    --back-mid: #0f1450;
    --back-bottom: #13245f;
    --magenta: #e0139f;
    --violet: #8a1bd8;
    --ink: #ffffff;
    --crop: #9a9a9a;
  }
  * { margin: 0; padding: 0; box-sizing: border-box; }
  html, body { width: 1200px; height: 3154px; overflow: hidden; }
  body {
    position: relative;
    background: var(--stage-dark);
    font-family: "Noto Sans", Verdana, sans-serif;
    color: var(--ink);
  }
  .print-sheet {
    position: absolute; left: 0; top: 1940px;
    width: 1200px; height: 1214px;
    background: var(--stage-light);
  }
  .card {
    position: absolute;
    width: 474px; height: 829px;
    overflow: hidden;
  }
  .card--shadow { box-shadow: 24px 30px 40px rgba(0,0,0,.55); }
  .card--front {
    background:
      radial-gradient(ellipse 90% 45% at 50% 100%, rgba(40,80,150,.45), transparent 70%),
      linear-gradient(180deg, var(--card-top) 0%, var(--card-mid) 50%, var(--card-bottom) 100%);
  }
  .card--back {
    background: linear-gradient(180deg, var(--back-top) 0%, #143a72 25%, var(--back-mid) 60%, var(--back-bottom) 100%);
  }
  .brand {
    position: absolute; left: 0; right: 0; top: 62px;
    text-align: center;
    font-family: "Rubik", Arial, sans-serif;
    font-weight: 500;
    font-size: 50px;
    letter-spacing: 2px;
    color: var(--magenta);
  }
  .holder { position: absolute; left: 0; right: 0; top: 226px; text-align: center; }
  .holder__name { font-size: 26px; font-weight: 400; letter-spacing: .5px; }
  .holder__name strong { font-weight: 700; }
  .holder__role {
    position: absolute; left: 270px; top: 36px;
    font-size: 8px; white-space: nowrap;
  }
  .divider {
    position: absolute; left: 168px; width: 138px; height: 3px;
    background: linear-gradient(90deg, var(--magenta), var(--violet));
  }
  .divider--mid { top: 361px; }
  .divider--foot { top: 822px; height: 8px; border-radius: 4px 4px 0 0; }
  .contact { position: absolute; left: 125px; font-size: 16px; display: flex; align-items: center; gap: 14px; white-space: nowrap; }
  .contact svg { width: 20px; height: 20px; flex: none; }
  .contact--phone { top: 436px; left: 126px; }
  .contact--mail { top: 469px; left: 124px; gap: 12px; }
  .icon-centre { position: absolute; left: 224px; width: 26px; height: 26px; }
  .icon-centre--pin { top: 602px; }
  .icon-centre--globe { top: 719px; }
  .line-centre { position: absolute; left: 0; right: 0; text-align: center; white-space: nowrap; }
  .address { top: 642px; font-size: 15px; letter-spacing: .2px; }
  .website { top: 755px; font-size: 21px; letter-spacing: .3px; }
  .back-pattern { position: absolute; inset: 0; }
  .back-brand {
    position: absolute; right: 40px; bottom: 40px;
    font-family: "Rubik", Arial, sans-serif; font-weight: 500;
    font-size: 22px; letter-spacing: 1px; color: var(--ink);
  }
  .crop { position: absolute; border-color: var(--crop); border-style: dotted; }
  .crop--v { top: 1984px; height: 1037px; width: 0; border-width: 0 0 0 1px; }
  .crop--h { left: 26px; width: 1148px; height: 0; border-width: 1px 0 0 0; }
  .safe-line { position: absolute; border: 1px solid rgba(255,255,255,.07); }
</style>
</head>
<body>

<!-- Presentation: front and back -->
<section class="card card--front card--shadow" style="left:59px; top:986px;">
  <div class="brand">TRIVELO</div>
  <div class="holder">
    <div class="holder__name">Florian <strong>GASTIER</strong></div>
    <div class="holder__role">Co-Founder &amp; CEO</div>
  </div>
  <div class="divider divider--mid"></div>
  <div class="contact contact--phone">
    <svg viewBox="0 0 24 24"><path fill="#e0139f" d="M6.6 10.8a15.1 15.1 0 0 0 6.6 6.6l2.2-2.2a1 1 0 0 1 1-.25 11.4 11.4 0 0 0 3.6.57 1 1 0 0 1 1 1V20a1 1 0 0 1-1 1A17 17 0 0 1 3 4a1 1 0 0 1 1-1h3.5a1 1 0 0 1 1 1c0 1.25.2 2.45.57 3.57a1 1 0 0 1-.25 1z"/></svg>
    <span>(+33) 6 52 84 26 07</span>
  </div>
  <div class="contact contact--mail">
    <svg viewBox="0 0 24 24"><rect x="2.5" y="5" width="19" height="14" fill="none" stroke="#e0139f" stroke-width="1.6"/><path d="M2.5 5l9.5 8 9.5-8" fill="none" stroke="#e0139f" stroke-width="1.6"/></svg>
    <span>florian@trivelo.example</span>
  </div>
  <svg class="icon-centre icon-centre--pin" viewBox="0 0 24 24"><path d="M12 2a7 7 0 0 0-7 7c0 5 7 13 7 13s7-8 7-13a7 7 0 0 0-7-7z" fill="none" stroke="#e0139f" stroke-width="1.8"/><circle cx="12" cy="9" r="2.6" fill="none" stroke="#e0139f" stroke-width="1.8"/></svg>
  <div class="line-centre address">17 rue des Tanneurs 69001 LYON</div>
  <svg class="icon-centre icon-centre--globe" viewBox="0 0 24 24" fill="none" stroke="#e0139f" stroke-width="1.6"><circle cx="12" cy="12" r="9.5"/><ellipse cx="12" cy="12" rx="4" ry="9.5"/><path d="M2.5 12h19M4 7h16M4 17h16"/></svg>
  <div class="line-centre website">www.trivelo.example</div>
  <div class="divider divider--foot"></div>
</section>

<section class="card card--back card--shadow" style="left:659px; top:986px;">
  <div class="back-pattern" role="img" aria-label="Repeating pattern of rounded blue bars fading from teal at the top to deep navy"></div>
  <div class="back-brand">TRIVELO</div>
</section>

<!-- Print layout with crop marks -->
<div class="print-sheet"></div>

<section class="card card--front" style="left:59px; top:2088px;">
  <div class="safe-line" style="left:9px; top:9px; right:9px; bottom:9px;"></div>
  <div class="brand">TRIVELO</div>
  <div class="holder">
    <div class="holder__name">Florian <strong>GASTIER</strong></div>
    <div class="holder__role">Co-Founder &amp; CEO</div>
  </div>
  <div class="divider divider--mid"></div>
  <div class="contact contact--phone">
    <svg viewBox="0 0 24 24"><path fill="#e0139f" d="M6.6 10.8a15.1 15.1 0 0 0 6.6 6.6l2.2-2.2a1 1 0 0 1 1-.25 11.4 11.4 0 0 0 3.6.57 1 1 0 0 1 1 1V20a1 1 0 0 1-1 1A17 17 0 0 1 3 4a1 1 0 0 1 1-1h3.5a1 1 0 0 1 1 1c0 1.250.2 2.45.57 3.57a1 1 0 0 1-.25 1z"/></svg>
    <span>(+33) 6 52 84 26 07</span>
  </div>
  <div class="contact contact--mail">
    <svg viewBox="0 0 24 24"><rect x="2.5" y="5" width="19" height="14" fill="none" stroke="#e0139f" stroke-width="1.6"/><path d="M2.5 5l9.5 8 9.5-8" fill="none" stroke="#e0139f" stroke-width="1.6"/></svg>
    <span>florian@trivelo.example</span>
  </div>
  <svg class="icon-centre icon-centre--pin" viewBox="0 0 24 24"><path d="M12 2a7 7 0 0 0-7 7c0 5 7 13 7 13s7-8 7-13a7 7 0 0 0-7-7z" fill="none" stroke="#e0139f" stroke-width="1.8"/><circle cx="12" cy="9" r="2.6" fill="none" stroke="#e0139f" stroke-width="1.8"/></svg>
  <div class="line-centre address">17 rue des Tanneurs 69001 LYON</div>
  <svg class="icon-centre icon-centre--globe" viewBox="0 0 24 24" fill="none" stroke="#e0139f" stroke-width="1.6"><circle cx="12" cy="12" r="9.5"/><ellipse cx="12" cy="12" rx="4" ry="9.5"/><path d="M2.5 12h19M4 7h16M4 17h16"/></svg>
  <div class="line-centre website">www.trivelo.example</div>
  <div class="divider divider--foot"></div>
</section>

<section class="card card--back" style="left:659px; top:2088px;">
  <div class="back-pattern" role="img" aria-label="Repeating pattern of rounded blue bars fading from teal at the top to deep navy"></div>
  <div class="safe-line" style="left:9px; top:9px; right:9px; bottom:9px;"></div>
  <div class="back-brand">TRIVELO</div>
</section>

<div class="crop crop--v" style="left:59px;"></div>
<div class="crop crop--v" style="left:72px;"></div>
<div class="crop crop--v" style="left:518px;"></div>
<div class="crop crop--v" style="left:533px;"></div>
<div class="crop crop--v" style="left:659px;"></div>
<div class="crop crop--v" style="left:674px;"></div>
<div class="crop crop--v" style="left:1118px;"></div>
<div class="crop crop--v" style="left:1131px;"></div>
<div class="crop crop--h" style="top:2088px;"></div>
<div class="crop crop--h" style="top:2103px;"></div>
<div class="crop crop--h" style="top:2901px;"></div>
<div class="crop crop--h" style="top:2916px;"></div>

</body>
</html>
```